Organic Infographic – "The 4 Dimensions of Transformation"

Overview:
We are a coaching/education brand (Brightmoor Institute) and need a redesigned infographic illustrating our 4-area transformation model. Our current version (attached) uses a rigid, hard-edged triangle/pyramid layout — we want a completely new visual approach that feels organic, soft, and alive, since the topic is human personal development, not a technical process.

Content structure (please keep the wording, redesign the visual form):

4 areas: "Embodiment – The Foundation" and "Focus & Intuition Redefined – The Lens" sit on the same base level. "Heart Centered Living – The Bridge" sits one level above, connecting/enabling the other two. "Becoming Unlimited – The Peak" sits at the top, made possible by Heart Centered Living.
The 4 areas influence and inspire one another — this mutual connection must be visually recognizable (e.g. through overlapping zones, blended color transitions, connecting flowing lines, or similar). Areas may stay visually distinct; the connection between them is what must be shown.
Hierarchy should be expressed mainly through position/arrangement (ascending flow), not through size differences — all 4 areas should carry similar visual weight, since each is equally essential.
A supporting element: "The Brightmoor Methodology" with 3 phases (Phase 1: Awareness & Insight, Phase 2: Integration & Practice, Phase 3: Expansion & Sustainable Growth), each with a short description (text provided below).

Style direction:
Organic, soft, flowing shapes — no sharp angles or rigid geometric triangles. Attached are 3 moodboard references showing the direction we like: overlapping/blended circular shapes, flowing ribbon-style connections, and organic swirl divisions. Please don't copy any of them directly — combine this organic/overlapping visual language with our specific asymmetric hierarchy (2 areas base level + 1 bridge + 1 peak), which none of the references show exactly. This creative translation is the core task.

Icons: Please design one new, unified icon per area (4 total) plus 3 simple icons for the methodology phases — consistent style across all 7, your creative interpretation is welcome.

Typography: Headlines in Arsenal, body text in DM Sans.

Colors: Base palette — Embodiment D09176, Focus & Intuition Redefined B6623E, Heart Centered Living D9866B, Becoming Unlimited 6F7A70, dark text 23211A, light accent EACEC1. Slight adjustments are welcome if they improve visual distinction between areas.

Technical requirements (important):

Final files as vector format (SVG, AI, or EPS), with separated, editable, non-flattened/non-merged layers and paths.
Shapes should consist of simple, closed outline paths — no fine textures, no complex multi-stop gradients, no photorealistic rendering — since the artwork will later be manually redrawn as a whiteboard-animation video.
Primary format: 16:9 landscape. A secondary vertical/mobile version (3 outer areas stacked below the top area) is welcome but optional.

Usage rights: Full commercial usage across website, video, and social media required.

Attachments to include: current draft PDF (for text content and logo reference only — not for layout), our logo file, and the 3 moodboard reference images.

Budget: $100–150 — please let us know if this realistically allows for more designer participation, or advise on adjusting scope/budget

Methodology phase texts (for the 3 supporting icons):

Phase 1: Awareness & Insight
Cultivating self-reflection, identifying patterns, and gaining clarity on personal drivers through introspective practices and data-informed assessment.

Phase 2: Integration & Practice
Applying tools and frameworks, developing new habits, and aligning actions with core values through consistent application and feedback loops.

Phase 3: Expansion & Sustainable Growth
Achieving long-term transformation, exceeding limitations, and fostering resilience through continuous evolution and a purpose-driven approach.

```html
<!DOCTYPE html>
<html lang="en">
<head>
<meta charset="utf-8">
<title>The 4 Dimensions of Transformation – Brightmoor Institute</title>
<link rel="stylesheet" href="https://fonts.googleapis.com/css2?family=Arsenal:wght@400;700&family=DM+Sans:wght@400;500;700&display=swap">
<style>
  :root {
    --peak: #6F7A70;
    --bridge: #D9866B;
    --foundation: #D09176;
    --lens: #B6623E;
    --ink: #23211A;
    --accent-light: #EACEC1;
    --pill: #F6E6DF;
    --rule: #D9866B;
    --arrow: #D39A82;
    --phase-1: #D6DCD2;
    --phase-2: #F2C2AC;
    --phase-3: #EBDAD0;
    --icon-dark: #9C3E1E;
    --icon-ink: #2E2C26;
    --white: #FFFFFF;
  }
  * { margin: 0; padding: 0; box-sizing: border-box; }
  html, body { width: 1200px; height: 678px; overflow: hidden; background: var(--white); }
  .canvas { position: relative; width: 1200px; height: 678px; font-family: "DM Sans", sans-serif; color: var(--ink); }
  .artwork { position: absolute; inset: 0; }

  .brand { position: absolute; left: 19px; top: 24px; display: flex; align-items: center; gap: 10px; }
  .brand-dot { width: 66px; height: 66px; border-radius: 50%; background: #C98266; }
  .brand-name { font-family: "Arsenal", sans-serif; font-weight: 400; font-size: 31px; color: var(--peak); letter-spacing: -0.3px; }

  .headline { position: absolute; left: 21px; top: 134px; font-family: "Arsenal", sans-serif; font-weight: 700; font-size: 34px; line-height: 40px; color: var(--ink); }
  .headline-rule { position: absolute; left: 20px; top: 229px; width: 77px; height: 2px; background: var(--rule); }
  .intro { position: absolute; left: 18px; top: 251px; font-size: 16px; line-height: 21px; font-weight: 500; color: var(--ink); }

  .area-label { position: absolute; text-align: center; color: var(--white); transform: translateX(-50%); white-space: nowrap; }
  .area-label .name { font-weight: 700; font-size: 18.5px; line-height: 22px; display: block; }
  .area-label .role { font-weight: 400; font-size: 16px; line-height: 20px; display: block; margin-top: 5px; }
  .area-peak { left: 484px; top: 196px; }
  .area-bridge { left: 462px; top: 390px; }
  .area-bridge .name { font-size: 20px; }
  .area-bridge .role { font-size: 17px; margin-top: 6px; }
  .area-foundation { left: 272px; top: 519px; }
  .area-foundation .name { font-size: 19px; }
  .area-foundation .role { font-size: 17px; margin-top: 5px; }
  .area-lens { left: 621px; top: 520px; }
  .area-lens .name { font-size: 18.5px; line-height: 21px; }

  .method-divider { position: absolute; left: 776px; top: 60px; width: 2px; height: 568px; background: var(--rule); }
  .method-title { position: absolute; left: 802px; top: 67px; width: 372px; height: 49px; border-radius: 25px; background: var(--pill);
    font-family: "Arsenal", sans-serif; font-weight: 700; font-size: 23px; line-height: 49px; padding-left: 35px; color: var(--ink); }

  .phase { position: absolute; left: 930px; width: 260px; }
  .phase-title { font-family: "Arsenal", sans-serif; font-weight: 700; font-size: 14.5px; line-height: 18px; color: var(--ink); white-space: nowrap; }
  .phase-text { font-size: 12.6px; line-height: 15.7px; margin-top: 7px; color: var(--ink); white-space: nowrap; }
  .phase-1 { top: 176px; }
  .phase-2 { top: 338px; }
  .phase-3 { top: 508px; }
  .phase-3 .phase-text { margin-top: 15px; }
</style>
</head>
<body>
<div class="canvas">
  <svg class="artwork" width="1200" height="678" viewBox="0 0 1200 678" aria-hidden="false">
    <defs>
      <marker id="arrowhead" viewBox="0 0 10 10" refX="7" refY="5" markerWidth="7" markerHeight="7" orient="auto-start-reverse">
        <path d="M0,0 L10,5 L0,10 L3,5 Z" fill="var(--arrow)"/>
      </marker>
    </defs>

    <!-- connecting arcs between the areas -->
    <g class="flow-arcs" fill="none" stroke="var(--arrow)" stroke-width="1.8">
      <path d="M352,240 Q292,290 272,360" marker-start="url(#arrowhead)" marker-end="url(#arrowhead)"/>
      <path d="M606,240 Q660,300 674,368" marker-start="url(#arrowhead)" marker-end="url(#arrowhead)"/>
      <path d="M382,601 Q448,622 514,601" marker-start="url(#arrowhead)" marker-end="url(#arrowhead)"/>
    </g>

    <!-- area discs -->
    <g class="area-discs">
      <circle class="disc-peak" cx="484" cy="176" r="108" fill="var(--peak)"/>
      <circle class="disc-foundation" cx="273" cy="506" r="113" fill="var(--foundation)"/>
      <circle class="disc-lens" cx="621" cy="516" r="108" fill="var(--lens)"/>
      <circle class="disc-bridge" cx="462" cy="384" r="120" fill="var(--bridge)" stroke="var(--white)" stroke-width="7"/>
    </g>

    <!-- peak icon area -->
    <g class="icon-peak" role="img" aria-label="Icon: figure with raised arms radiating light">
      <circle cx="479" cy="142" r="38" fill="var(--white)" opacity="0.14"/>
    </g>

    <!-- bridge icon: heart with rays -->
    <g class="icon-bridge" fill="none" stroke="var(--white)" stroke-width="3" stroke-linecap="round" stroke-linejoin="round">
      <path d="M462,380 C448,368 436,360 436,348 C436,340 442,334 450,334 C456,334 460,338 462,343 C464,338 468,334 474,334 C482,334 488,340 488,348 C488,360 476,368 462,380 Z"/>
      <line x1="462" y1="303" x2="462" y2="318"/>
      <line x1="441" y1="308" x2="447" y2="321"/>
      <line x1="483" y1="308" x2="477" y2="321"/>
      <line x1="423" y1="321" x2="434" y2="330"/>
      <line x1="501" y1="321" x2="490" y2="330"/>
      <line x1="413" y1="339" x2="427" y2="343"/>
      <line x1="511" y1="339" x2="497" y2="343"/>
      <line x1="413" y1="358" x2="427" y2="357"/>
      <line x1="511" y1="358" x2="497" y2="357"/>
    </g>

    <!-- foundation icon area -->
    <g class="icon-foundation" role="img" aria-label="Icon: figure rising from open leaves">
      <circle cx="273" cy="466" r="40" fill="var(--white)" opacity="0.14"/>
    </g>

    <!-- lens icon: eye with rays -->
    <g class="icon-lens" fill="none" stroke="var(--white)" stroke-width="3" stroke-linecap="round" stroke-linejoin="round">
      <path d="M585,492 Q621,455 657,492 Q621,529 585,492 Z"/>
      <circle cx="621" cy="492" r="12"/>
      <circle cx="621" cy="492" r="4.5" fill="var(--white)" stroke="none"/>
      <line x1="621" y1="441" x2="621" y2="455"/>
      <line x1="602" y1="446" x2="608" y2="458"/>
      <line x1="640" y1="446" x2="634" y2="458"/>
      <line x1="586" y1="456" x2="596" y2="464"/>
      <line x1="656" y1="456" x2="646" y2="464"/>
    </g>

    <!-- methodology phase discs -->
    <g class="phase-discs">
      <circle cx="858" cy="220" r="53" fill="var(--phase-1)"/>
      <circle cx="858" cy="381" r="53" fill="var(--phase-2)"/>
      <circle cx="858" cy="545" r="53" fill="var(--phase-3)"/>
    </g>
    <g class="phase-links" stroke="var(--rule)" stroke-width="2" stroke-dasharray="4 4">
      <line x1="858" y1="283" x2="858" y2="320"/>
      <line x1="858" y1="445" x2="858" y2="483"/>
    </g>

    <!-- phase 1 icon area -->
    <g class="icon-phase-1" role="img" aria-label="Icon: mind with a growing seedling">
      <circle cx="858" cy="220" r="32" fill="var(--white)" opacity="0.35"/>
    </g>

    <!-- phase 2 icon: gears -->
    <g class="icon-phase-2" fill="none" stroke="var(--icon-dark)" stroke-linecap="butt">
      <circle cx="874" cy="370" r="17" stroke-width="5" stroke-dasharray="5.3 3.6"/>
      <circle cx="874" cy="370" r="14" stroke-width="2.5"/>
      <circle cx="874" cy="370" r="6" stroke-width="2.5"/>
      <circle cx="843" cy="395" r="16" stroke-width="5" stroke-dasharray="5 3.4"/>
      <circle cx="843" cy="395" r="13" stroke-width="2.5"/>
      <circle cx="843" cy="395" r="5.5" stroke-width="2.5"/>
    </g>

    <!-- phase 3 icon: sprout -->
    <g class="icon-phase-3" fill="none" stroke="var(--icon-ink)" stroke-width="2.4" stroke-linecap="round" stroke-linejoin="round">
      <path d="M858,575 L858,548"/>
      <path d="M858,560 Q845,540 832,537 Q830,556 852,562"/>
      <path d="M858,552 Q866,532 884,530 Q882,552 862,556"/>
      <path d="M830,570 Q848,566 858,575 Q868,566 886,570"/>
      <line x1="858" y1="510" x2="858" y2="520"/>
      <line x1="842" y1="516" x2="848" y2="523"/>
      <line x1="874" y1="516" x2="868" y2="523"/>
    </g>
  </svg>

  <div class="brand">
    <span class="brand-dot"></span>
    <span class="brand-name">Brightmoor Institute</span>
  </div>

  <h1 class="headline">The 4 Dimensions<br>of Transformation</h1>
  <div class="headline-rule"></div>
  <p class="intro">A holistic, interconnected<br>path to a more conscious<br>fulfilling and limitless you.</p>

  <div class="area-label area-peak"><span class="name">Becoming Unlimited</span><span class="role">The Peak</span></div>
  <div class="area-label area-bridge"><span class="name">Heart Centered Living</span><span class="role">The Bridge</span></div>
  <div class="area-label area-foundation"><span class="name">Embodiment</span><span class="role">The Foundation</span></div>
  <div class="area-label area-lens"><span class="name">Focus &amp; Intuition<br>Redefined</span><span class="role">The Lens</span></div>

  <div class="method-divider"></div>
  <h2 class="method-title">The Brightmoor Methodology</h2>

  <div class="phase phase-1">
    <h3 class="phase-title">Phase 1: Awareness &amp; Insight</h3>
    <p class="phase-text">Cultivating self-reflection, identifying<br>patterns, and gaining clarity on personal<br>drivers through introspective practices<br>and data-informed assessment.</p>
  </div>
  <div class="phase phase-2">
    <h3 class="phase-title">Phase 2: Integration &amp; Practice</h3>
    <p class="phase-text">Applying tools and frameworks,<br>developing new habits, and aligning<br>actions with core values through<br>consistent application and feedback<br>loops.</p>
  </div>
  <div class="phase phase-3">
    <h3 class="phase-title">Phase 3: Expansion &amp; Sustainable Growth</h3>
    <p class="phase-text">Achieving long-term transformation,<br>exceeding limitations, and fostering<br>resilience through continuous evolution<br>and a purpose-driven approach.</p>
  </div>
</div>
</body>
</html>
```